Legal Stationary

A full set of stationery is required
The image and logo, along with colour, are set and attached.
The style should be modern, clean, and corporate. Not just a basic template off the web.
In addition to the address/website/email/phone fields for DX and KWT number, with the text “the firm is authorised and regulated by the KWT”
All files in all formats will be needed to allow editing after. Initial setup of templates will be required, and details for 4 business cards will be supplied.
Target Market(s)
Consumers of legal services
Industry/Entity Type
Legal

```html
<!DOCTYPE html>
<html lang="en">
<head>
<meta charset="utf-8">
<title>Harwell Law – Stationery Set</title>
<link href="https://fonts.googleapis.com/css2?family=Montserrat:wght@500;600&family=Nunito+Sans:wght@400;600&display=swap" rel="stylesheet">
<style>
  :root{
    --brand:#2a3c92;
    --brand-text:#2e3f9a;
    --paper:#ffffff;
    --paper-shade:#f4f4f6;
    --rule:#b9b9c0;
    --ink:#3a3a44;
    --flap-dark:#2a2a2c;
    --mark-faint:#eef0f7;
    --backdrop:#e6e4e1;
  }
  *{box-sizing:border-box;margin:0;padding:0}
  html,body{width:1200px;height:522px;overflow:hidden;background:var(--backdrop)}
  body{position:relative;font-family:"Nunito Sans",sans-serif;color:var(--ink)}

  .sheet{position:absolute;background:var(--paper);overflow:hidden;box-shadow:0 1px 3px rgba(0,0,0,.25)}
  .sheet--letterhead{left:24px;top:39px;width:340px;height:440px}
  .sheet--fax{left:378px;top:42px;width:340px;height:440px}

  .band{position:absolute;left:0;top:0;width:100%;height:31px;background:var(--brand);color:#fff}
  .wordmark{font-family:"Montserrat",sans-serif;font-weight:500;color:#fff;white-space:nowrap;letter-spacing:.3px}
  .band .wordmark{position:absolute;left:7px;top:8px;font-size:13px}
  .band__contact{position:absolute;right:10px;font-size:5px;text-align:right;line-height:1;white-space:nowrap}
  .band__address{top:10px}
  .band__lines{top:20px;word-spacing:1px}
  .band__lines span{margin-left:9px}

  .watermark{position:absolute;left:50%;top:53%;transform:translate(-50%,-50%) rotate(-55deg);
    font-family:"Montserrat",sans-serif;font-weight:600;font-size:42px;color:var(--mark-faint);white-space:nowrap}

  .sheet__foot{position:absolute;left:6px;right:10px;top:417px;border-top:1px solid #e2e2e6}
  .sheet__foot p{position:absolute;top:9px;font-size:6px;color:var(--brand-text);white-space:nowrap}
  .sheet__foot .left{left:0}
  .sheet__foot .right{right:0}

  .fax__title{position:absolute;left:16px;top:73px;font-size:27px;color:var(--brand-text);font-weight:400}
  .fax__field{position:absolute;height:9px;border-bottom:.7px solid var(--rule);font-size:6.5px;line-height:8px}
  .fax__field--left{left:15px;width:183px}
  .fax__field--right{left:198px;width:124px}
  .fax__checks{position:absolute;left:15px;top:207px;width:320px;display:flex;justify-content:space-between;font-size:6.5px}
  .fax__checks span{display:flex;align-items:center;gap:4px}
  .fax__checks i{display:inline-block;width:7px;height:7px;border:.8px solid #555}

  .envelope{position:absolute;background:var(--paper);box-shadow:0 1px 3px rgba(0,0,0,.25);overflow:hidden}
  .envelope--back{left:796px;top:42px;width:380px;height:170px}
  .envelope--middle{left:784px;top:116px;width:380px;height:170px;background:var(--paper-shade)}
  .envelope svg.flap{position:absolute;left:0;top:0}
  .envelope--back .wordmark{position:absolute;left:129px;top:22px;font-size:22px;color:var(--brand)}
  .envelope--middle .wordmark{position:absolute;left:134px;top:16px;font-size:22px;color:#8e8e90}
  .envelope--front{left:758px;top:202px;width:380px;height:169px}
  .envelope--front .band .wordmark{left:9px;top:7px;font-size:16px}
  .envelope--front .band__contact{right:5px;font-size:5px}
  .envelope--front .band__address{top:9px}
  .envelope--front .band__lines{top:18px}
  .envelope__web{position:absolute;left:0;right:0;bottom:0;height:15px;border-top:.7px solid #e0e0e4;font-size:5.2px;letter-spacing:.6px;padding-left:8px;display:flex;align-items:center;gap:3px}

  .card{position:absolute;top:400px;height:79px;box-shadow:0 1px 3px rgba(0,0,0,.25);overflow:hidden}
  .card--contact{left:741px;width:138px;background:var(--paper);border:3px solid var(--brand)}
  .card--contact .wordmark{position:absolute;left:6px;top:20px;font-size:8.5px;color:var(--brand)}
  .card__claim{position:absolute;left:6px;top:34px;width:62px;font-size:4.3px;line-height:1.4;color:var(--brand-text)}
  .card__person{position:absolute;left:84px;top:9px;font-size:4.6px;color:var(--brand-text);font-weight:600}
  .card__role{position:absolute;left:84px;top:15px;font-size:3px;color:#666}
  .card__info{position:absolute;left:84px;top:28px;font-size:3.6px;line-height:8.6px;color:#333;list-style:none}
  .card__info li{display:flex;align-items:center;gap:3px}
  .card__address{position:absolute;left:0;right:0;bottom:0;height:13px;border-top:.7px solid #ddd;font-size:3.7px;display:flex;align-items:center;justify-content:center;gap:2px;color:#333}

  .card--legal{left:886px;width:134px;background:var(--brand);color:#fff;font-size:5px;text-align:right}
  .card--legal .wordmark{position:absolute;left:5px;top:6px;bottom:6px;writing-mode:vertical-rl;transform:rotate(180deg);font-size:8.5px;text-align:center}
  .card--legal .card__reg{position:absolute;right:6px;top:6px;line-height:1.5}
  .card--legal .card__web{position:absolute;right:6px;bottom:6px;letter-spacing:.6px}

  .card--brand{left:1034px;width:140px;background:var(--brand);color:#fff;text-align:center}
  .card--brand .wordmark{position:absolute;left:0;right:0;top:26px;font-size:14px}
  .card--brand .card__web{position:absolute;left:0;right:0;top:47px;font-size:4.6px;letter-spacing:.8px}
  .ico{display:inline-block;vertical-align:middle;flex:none}
</style>
</head>
<body>

<section class="sheet sheet--letterhead" aria-label="Letterhead">
  <header class="band">
    <span class="wordmark">HARWELL LAW</span>
    <p class="band__contact band__address">Street Name, City Name, State Zipcode
      <svg class="ico" width="5" height="5" viewBox="0 0 10 10"><path d="M5 0a3.5 3.5 0 0 0-3.5 3.5C1.5 6 5 10 5 10s3.5-4 3.5-6.5A3.5 3.5 0 0 0 5 0z" fill="#fff"/></svg></p>
    <p class="band__contact band__lines">123.456.7890<span>inquiry@harwelllaw.com</span><span>www.harwelllaw.com</span></p>
  </header>
  <div class="watermark" aria-hidden="true">HARWELL LAW</div>
  <footer class="sheet__foot">
    <p class="left">DX No. 7318042 &amp; KWT No. 552913</p>
    <p class="right">The Firm Is Authorised And Regulated By The KWT</p>
  </footer>
</section>

<section class="sheet sheet--fax" aria-label="Fax cover sheet">
  <header class="band">
    <span class="wordmark">HARWELL LAW</span>
    <p class="band__contact band__address">Street Name, City Name, State Zipcode
      <svg class="ico" width="5" height="5" viewBox="0 0 10 10"><path d="M5 0a3.5 3.5 0 0 0-3.5 3.5C1.5 6 5 10 5 10s3.5-4 3.5-6.5A3.5 3.5 0 0 0 5 0z" fill="#fff"/></svg></p>
    <p class="band__contact band__lines">123.456.7890<span>inquiry@harwelllaw.com</span><span>www.harwelllaw.com</span></p>
  </header>
  <div class="watermark" aria-hidden="true">HARWELL LAW</div>
  <h1 class="fax__title">FAX</h1>
  <p class="fax__field fax__field--left" style="top:117px">To :</p>
  <p class="fax__field fax__field--right" style="top:117px">From :</p>
  <p class="fax__field fax__field--left" style="top:136px">Fax :</p>
  <p class="fax__field fax__field--right" style="top:136px">Pages :</p>
  <p class="fax__field fax__field--left" style="top:155px">Phone :</p>
  <p class="fax__field fax__field--right" style="top:155px">Date :</p>
  <p class="fax__field fax__field--left" style="top:174px">Re :</p>
  <p class="fax__field fax__field--right" style="top:174px">CC :</p>
  <div class="fax__checks">
    <span><i></i>Urgent</span><span><i></i>For Review</span><span><i></i>Please Comment</span><span><i></i>Please Reply</span><span><i></i>Please Recycle</span>
  </div>
  <footer class="sheet__foot">
    <p class="left">DX No. 7318042 &amp; KWT No. 552913</p>
    <p class="right">The Firm Is Authorised And Regulated By The KWT</p>
  </footer>
</section>

<section class="envelope envelope--back" aria-label="Envelope back, open flap">
  <svg class="flap" width="380" height="170" viewBox="0 0 380 170"><path d="M2 0C6 25 12 30 40 34L180 66Q192 69 204 66L350 34C372 30 376 20 380 0" fill="none" stroke="var(--brand)" stroke-width=".8"/></svg>
  <span class="wordmark">HARWELL LAW</span>
</section>

<section class="envelope envelope--middle" aria-label="Envelope back, dark flap">
  <svg class="flap" width="380" height="170" viewBox="0 0 380 170"><path d="M0 0H380C376 25 370 32 340 38L200 66Q190 68 180 66L40 38C12 32 6 25 0 0Z" fill="var(--flap-dark)"/></svg>
  <span class="wordmark">HARWELL LAW</span>
</section>

<section class="envelope envelope--front" aria-label="Envelope front">
  <header class="band">
    <span class="wordmark">HARWELL LAW</span>
    <p class="band__contact band__address">DX No. 7318042 &amp; KWT No. 552913</p>
    <p class="band__contact band__lines">The Firm Is Authorised And Regulated By The KWT</p>
  </header>
  <p class="envelope__web">
    <svg class="ico" width="6" height="6" viewBox="0 0 10 10"><circle cx="5" cy="5" r="4.3" fill="none" stroke="var(--brand)" stroke-width="1"/><path d="M.7 5h8.6M5 .7c-2.4 2.4-2.4 6.2 0 8.6M5 .7c2.4 2.4 2.4 6.2 0 8.6" fill="none" stroke="var(--brand)" stroke-width=".8"/></svg>
    <span>www.harwelllaw.com</span></p>
</section>

<section class="card card--contact" aria-label="Business card front">
  <span class="wordmark">HARWELL LAW</span>
  <p class="card__claim">The Firm Is Authorised And Regulated By The KWT</p>
  <p class="card__person">Your Name</p>
  <p class="card__role">Designation</p>
  <ul class="card__info">
    <li><svg class="ico" width="4" height="4" viewBox="0 0 10 10"><circle cx="5" cy="5" r="4.3" fill="none" stroke="var(--brand)"/></svg>123.456.7890</li>
    <li><svg class="ico" width="4" height="4" viewBox="0 0 10 10"><rect x="1" y="2" width="8" height="6" fill="var(--brand)"/></svg>inquiry@harwelllaw.com</li>
    <li><svg class="ico" width="4" height="4" viewBox="0 0 10 10"><circle cx="5" cy="5" r="4.3" fill="none" stroke="var(--brand)"/></svg>www.harwelllaw.com</li>
  </ul>
  <p class="card__address">
    <svg class="ico" width="4" height="4" viewBox="0 0 10 10"><path d="M5 0a3.5 3.5 0 0 0-3.5 3.5C1.5 6 5 10 5 10s3.5-4 3.5-6.5A3.5 3.5 0 0 0 5 0z" fill="var(--brand)"/></svg>
    <span>Street Name, City Name State Zipcode</span></p>
</section>

<section class="card card--legal" aria-label="Business card back">
  <span class="wordmark">HARWELL LAW</span>
  <p class="card__reg">DX No. 7318042 &amp; KWT No. 552913<br>The Firm Is Authorised And Regulated<br>By The KWT</p>
  <p class="card__web">www.harwelllaw.com</p>
</section>

<section class="card card--brand" aria-label="Business card brand side">
  <span class="wordmark">HARWELL LAW</span>
  <p class="card__web">www.harwelllaw.com</p>
</section>

</body>
</html>
```